Logo & Visitenkarte für Weinbauer
Zielgruppe
Ich bin Weinbauer und betreibe auch einen Buschenschank. Zielgruppe ist die Gastronomie und der (Durchschnitts-) Endverbraucher.
Aufgabenstellung
Unsere Betriebsstätte ist im Rebhügelgau Weinviertel (Österreich).
Wir wollen die Werte Tradition, Regional, Vertrauen und Bodenständigkeit vermitteln.
Unsere Kunden schätzen die Herkunft.
Das Logo soll als Firmenlogo und auch für die Weinetiketten verwendet werden können.

```html
<!DOCTYPE html>
<html lang="de">
<head>
<meta charset="utf-8">
<title>Weingut Orlitzer – Visitenkarte</title>
<link rel="stylesheet" href="https://fonts.googleapis.com/css2?family=Raleway:wght@300;400&display=swap">
<style>
  :root {
    --paper: #ffffff;
    --ink: #161616;
    --edge: #c8c8c8;
    --gold-deep: #b88a34;
    --gold: #e2c36f;
    --gold-light: #fbefb8;
    --gold-pale: #dcd4b0;
  }
  html, body {
    margin: 0;
    padding: 0;
    width: 1200px;
    height: 777px;
    overflow: hidden;
    background: var(--paper);
  }
  .card {
    position: relative;
    width: 1200px;
    height: 777px;
    box-sizing: border-box;
    border: 2px solid var(--edge);
    background: var(--paper);
    font-family: "Raleway", Arial, sans-serif;
    font-weight: 300;
    color: var(--ink);
  }
  .card__frame {
    position: absolute;
    left: 36px;
    top: 36px;
    width: 1128px;
    height: 704px;
  }
  .brand-mark {
    position: absolute;
    left: 190px;
    top: 140px;
    width: 290px;
    height: 290px;
    border-radius: 50%;
    background: linear-gradient(135deg, var(--gold-pale) 0%, var(--gold) 40%, var(--gold-light) 65%, var(--gold-deep) 100%);
  }
  .brand-name {
    position: absolute;
    left: 115px;
    width: 430px;
    top: 572px;
    text-align: center;
    font-size: 64px;
    font-weight: 300;
    letter-spacing: 1px;
    line-height: 1;
    margin: 0;
  }
  .brand-tagline {
    position: absolute;
    left: 114px;
    top: 674px;
    font-size: 31px;
    line-height: 1;
    margin: 0;
  }
  .contact {
    position: absolute;
    left: 645px;
    top: 413px;
    font-size: 31px;
    font-style: normal;
    line-height: 42px;
    margin: 0;
  }
  .contact p { margin: 0; }
  .contact .contact__hours { margin-top: 42px; }
</style>
</head>
<body>
  <main class="card">
    <svg class="card__frame" viewBox="0 0 1128 704" aria-hidden="true">
      <defs>
        <linearGradient id="frameGold" x1="0" y1="0" x2="1" y2="0">
          <stop offset="0" stop-color="#e6c46a"/>
          <stop offset="0.35" stop-color="#c69a45"/>
          <stop offset="0.55" stop-color="#b48a3c"/>
          <stop offset="0.8" stop-color="#fbf0c0"/>
          <stop offset="1" stop-color="#e4c26c"/>
        </linearGradient>
      </defs>
      <rect x="1" y="1" width="1126" height="702" fill="none" stroke="url(#frameGold)" stroke-width="2.5"/>
    </svg>

    <div class="brand-mark" role="img" aria-label="Platz für das Markenzeichen des Weinguts"></div>
    <p class="brand-name">Orlitzer</p>
    <p class="brand-tagline">Weinbau &amp; Buschenschank</p>

    <address class="contact">
      <p>WEINGUT ORLITZER</p>
      <p>3712 Lindenau am Rebweg 14</p>
      <p>info@wein-orlitzer.at</p>
      <p class="contact__hours">Weinverkauf ab Hof jederzeit nach</p>
      <p>Terminvereinbarung:</p>
      <p>+43 660 12 34 567</p>
    </address>
  </main>
</body>
</html>
```